Wren's Hearth Support Business Card

Business card design
Font must be in Poppins Regular for Wren's Hearth Support
Safe Days Ahead font is Alex Brush

Colour must be Hex #910E2B
RGB 145-14-43
Pantone 7427 C
We want the card editable
On the front please include
Name eg Mavis Dunleavy
Position eg Clinical Care Manager
Phone number mobile 0473 856 342
Phone 08 7394 2650
Email : mavis@wrenshearthsupport.com.au
Address : Gullwing Cove, Coral Coast, 6291
Website : wrenshearthsupport.com.au
Contact us today to experience the warmth, respect and personal touch of Wren's Hearth Support.

Target Market(s)

35+

Industry/Entity Type

aged care / community

Contact Information for Business Card

see project description

Requirements
Must have
• Colours, logos and fonts as detailed and uploaded

```html
<!DOCTYPE html>
<html lang="en">
<head>
<meta charset="utf-8">
<title>Wren's Hearth Support – Business Card</title>
<link href="https://fonts.googleapis.com/css2?family=Alex+Brush&family=Montserrat:ital,wght@0,400;0,600;1,700&family=Poppins:wght@400&display=swap" rel="stylesheet">
<style>
  :root {
    --brand: #910E2B;
    --white: #ffffff;
    --stage: #b9b9b9;
    --blush: #f1e1e4;
  }
  * { box-sizing: border-box; margin: 0; padding: 0; }
  html, body { width: 1200px; height: 1200px; overflow: hidden; }
  body { background: var(--stage); position: relative; font-family: "Montserrat", sans-serif; }

  .card { position: absolute; left: 150px; width: 898px; height: 524px; overflow: hidden; }
  .card--front { top: 56px; background: var(--brand); color: var(--white); }
  .card--back { top: 620px; background: var(--white); }

  .holder__name { position: absolute; left: 64px; top: 98px; font-weight: 600; font-size: 36px; letter-spacing: 0.5px; line-height: 1; }
  .holder__role { position: absolute; left: 64px; top: 146px; font-size: 23px; font-weight: 400; line-height: 1.2; }

  .contact-list { position: absolute; left: 50px; top: 272px; list-style: none; }
  .contact-list li { display: flex; align-items: center; height: 34.5px; font-size: 23px; }
  .contact-list svg { width: 18px; height: 18px; margin-right: 21px; fill: var(--white); flex: none; }
  .contact-list .contact--web { margin-top: 19px; font-weight: 700; font-style: italic; }

  .front-mark { position: absolute; left: 566px; top: 89px; width: 250px; height: 250px; border: 11px solid var(--white); border-radius: 50%; display: flex; align-items: center; justify-content: center; text-align: center; font-family: "Poppins", sans-serif; font-size: 26px; line-height: 1.2; color: var(--white); }

  .back-decor { position: absolute; left: 540px; top: -40px; width: 420px; height: 420px; border-radius: 50%; background: var(--blush); }

  .brand-lockup { position: absolute; left: 78px; top: 193px; display: flex; align-items: center; }
  .brand-lockup__circle { width: 124px; height: 124px; border: 7px solid var(--brand); border-radius: 50%; margin-right: 18px; flex: none; }
  .brand-lockup__name { font-family: "Poppins", sans-serif; font-weight: 400; font-size: 43px; line-height: 1.05; color: var(--brand); }
  .brand-lockup__tagline { font-family: "Alex Brush", cursive; font-size: 30px; color: var(--brand); margin-top: 6px; }
</style>
</head>
<body>

<section class="card card--front" aria-label="Card front">
  <h1 class="holder__name">MAVIS DUNLEAVY</h1>
  <p class="holder__role">Position eg Clinical Care Manager</p>

  <ul class="contact-list">
    <li><svg viewBox="0 0 24 24" aria-hidden="true"><path d="M7 1h10a2 2 0 0 1 2 2v18a2 2 0 0 1-2 2H7a2 2 0 0 1-2-2V3a2 2 0 0 1 2-2zm0 3v14h10V4z"/></svg>0473 856 342</li>
    <li><svg viewBox="0 0 24 24" aria-hidden="true"><path d="M6.6 10.8a15 15 0 0 0 6.6 6.6l2.2-2.2a1 1 0 0 1 1-.25 11.4 11.4 0 0 0 3.6.57 1 1 0 0 1 1 1V20a1 1 0 0 1-1 1A17 17 0 0 1 3 4a1 1 0 0 1 1-1h3.5a1 1 0 0 1 1 1c0 1.25.2 2.45.57 3.57a1 1 0 0 1-.25 1z"/></svg>08 7394 2650</li>
    <li><svg viewBox="0 0 24 24" aria-hidden="true"><path d="M3 5h18v14H3zm2 2v.5l7 4.5 7-4.5V7l-7 4.5z"/></svg>mavis@wrenshearthsupport.com.au</li>
    <li><svg viewBox="0 0 24 24" aria-hidden="true"><path d="M12 2a7 7 0 0 0-7 7c0 5 7 13 7 13s7-8 7-13a7 7 0 0 0-7-7zm0 9.5A2.5 2.5 0 1 1 12 6.5a2.5 2.5 0 0 1 0 5z"/></svg>Gullwing Cove, Coral Coast, 6291</li>
    <li class="contact--web"><svg viewBox="0 0 24 24" aria-hidden="true"><path d="M12 2a10 10 0 1 0 0 20 10 10 0 0 0 0-20zm6.9 9h-3a15 15 0 0 0-1.2-5.6A8 8 0 0 1 18.9 11zM12 4c.9 1.3 1.8 3.8 1.9 7h-3.8c.1-3.2 1-5.7 1.9-7zM9.3 5.4A15 15 0 0 0 8.1 11h-3a8 8 0 0 1 4.2-5.6zM5.1 13h3a15 15 0 0 0 1.2 5.6A8 8 0 0 1 5.1 13zM12 20c-.9-1.3-1.8-3.8-1.9-7h3.8c-.1 3.2-1 5.7-1.9 7zm2.7-1.4a15 15 0 0 0 1.2-5.6h3a8 8 0 0 1-4.2 5.6z"/></svg>wrenshearthsupport.com.au</li>
  </ul>

  <div class="front-mark">Wren's Hearth<br>Support</div>
</section>

<section class="card card--back" aria-label="Card back">
  <div class="back-decor" role="img" aria-label="Faint brand decoration"></div>
  <div class="brand-lockup">
    <div class="brand-lockup__circle"></div>
    <div>
      <p class="brand-lockup__name">Wren's Hearth<br>Support</p>
      <p class="brand-lockup__tagline">Safe Days Ahead</p>
    </div>
  </div>
</section>

</body>
</html>
```